Medical Implant company needs a Top Quality Premium Brochure

We need to create a top quality brochure for VIP clients, formed by top spine surgeons. The main goal here is to cause a deep quality impact, positioning the company and it´s solutions above the others, with a refined, unique and creative material.

Special paper, hot stamping, innovative format are welcome.

For more information check out our website: www.velcorasurg.com.br (web translator are recommended for content understanding)

Velcorasurg works with top quality spine and pain management products, providing solutions for the medical specialists, investing in high quality processes and continued medical education.

Short briefing:
1 - Company profile
2 - Quality / vision
3 - Continued education programs
4 - Main products
5 - Main partners
6 - Final stuff (creative final thoughts / considerations)

FORMAT: 25 x 18,5 cm (horizontal)
PAGES - 16

REFERENCES:

https://www.portfoliqo.net/gallery/20417839/Medical-Healthcare-Profile-Brochure

https://www.portfoliqo.net/gallery/7162904/KT-Alpine-Style-Brochure

Target Market(s)

Mainly brazilian spine and neuro surgeons with minimally invasive surgery skills.

Industry/Entity Type

Education

Requirements
Must have

• 18 pages design

1. Cover
2. IMAGE + TITLE - About Us
3. IMAGE + TEXT - About Us
4. IMAGE + TITLE - Vision
5. IMAGE + TEXT - Vision
6. IMAGE + TITLE - Quality
7. IMAGE + TEXT - Quality
8. Timeline Left
9. Timeline Right
10. IMAGE + TITLE - Medical Education
11. IMAGE + TEXT - Medical Education
12. IMAGE + TITLE - Minimally Invasive Technology
13. IMAGE + TEXT - Minimally Invasive Technology
14. IMAGE + TITLE - Impact Phrase
15. IMAGE + TEXT - Impact Phrase
16. Back

As longs as the text is under development and will be placed internally in the winning design, please use 'lorem ipsum' for text areas. The titles can follow the index above.

Nice to have
• The use of office pictures with some style / artistic finish in pages "about us"

```html
<!DOCTYPE html>
<html lang="en">
<head>
<meta charset="utf-8">
<title>Velcorasurg Brochure – Contents Spread</title>
<link rel="stylesheet" href="https://fonts.googleapis.com/css2?family=Exo+2:ital,wght@0,400;0,600;0,700;1,600&family=Open+Sans:wght@400;600&display=swap">
<style>
  :root {
    --green: #14a04f;
    --green-dark: #0e8a42;
    --ink: #4a4a4a;
    --paper: #ffffff;
    --backdrop: #e4e4e4;
  }
  * { margin: 0; padding: 0; box-sizing: border-box; }
  html, body { width: 1200px; height: 900px; overflow: hidden; }
  body {
    background: var(--backdrop);
    font-family: "Open Sans", sans-serif;
    position: relative;
  }
  .spread {
    position: absolute;
    left: 50px; top: 246px;
    width: 1100px; height: 407px;
    display: flex;
    box-shadow: 0 10px 30px rgba(0,0,0,.18);
  }
  .page {
    position: relative;
    width: 550px; height: 407px;
    background: var(--paper);
    overflow: hidden;
  }
  .page--left { background: linear-gradient(to right, #fff 88%, #f0f0f0); }
  .page--right { background: linear-gradient(to left, #fff 90%, #ececec); }

  .section-tab {
    position: absolute;
    height: 24px;
    background: var(--green);
    color: #fff;
    font-family: "Exo 2", sans-serif;
    font-size: 9px;
    letter-spacing: .08em;
    text-transform: uppercase;
    display: flex; align-items: center;
    padding: 0 14px;
  }
  .page--left .section-tab { left: 230px; top: 0; width: 170px; }
  .page--right .section-tab { right: 0; top: 118px; width: 170px; justify-content: flex-end; }

  .contents-title {
    position: absolute;
    left: 60px; top: 40px;
    font-family: "Exo 2", sans-serif;
    font-style: italic;
    font-weight: 600;
    font-size: 46px;
    color: var(--green);
    letter-spacing: .01em;
  }
  .toc {
    position: absolute;
    list-style: none;
    width: 210px;
  }
  .toc--first { left: 60px; top: 108px; }
  .toc--second { left: 300px; top: 200px; }
  .toc__item { margin-bottom: 10px; }
  .toc__title {
    font-family: "Exo 2", sans-serif;
    font-weight: 700;
    font-size: 10.5px;
    color: var(--green);
    line-height: 1.2;
  }
  .toc__num { margin-right: 3px; }
  .toc__text {
    font-size: 6.5px;
    color: var(--ink);
    line-height: 1.4;
  }

  .page-number {
    position: absolute;
    bottom: 14px;
    width: 16px; height: 16px;
    background: var(--green);
    color: #fff;
    font-family: "Exo 2", sans-serif;
    font-size: 8px;
    display: flex; align-items: center; justify-content: center;
  }
  .page--left .page-number { left: 30px; }
  .page--right .page-number { right: 30px; }

  .photo {
    position: absolute;
    border: 3px solid #fff;
    box-shadow: 0 1px 3px rgba(0,0,0,.12);
  }
  .photo__num {
    position: absolute;
    left: -3px; bottom: -3px;
    width: 18px; height: 18px;
    background: var(--green);
    color: #fff;
    font-family: "Exo 2", sans-serif;
    font-size: 8px;
    display: flex; align-items: center; justify-content: center;
  }
  .photo--doctor-notes { left: 110px; top: 28px; width: 140px; height: 112px; background: linear-gradient(135deg, #e9eef2, #c9d6df 60%, #8fb6c9); }
  .photo--dental { left: 258px; top: 28px; width: 112px; height: 112px; background: linear-gradient(160deg, #f4f4f4, #e2d4cc 55%, #7a5a4a); }
  .photo--patient-chat { left: 28px; top: 150px; width: 124px; height: 92px; background: linear-gradient(135deg, #dfe5e8, #9fb3bc 50%, #4fb3c2); }
  .photo--stethoscope { left: 160px; top: 150px; width: 140px; height: 200px; background: linear-gradient(150deg, #8fc9a4, #2f9a5c 55%, #1e7a44); }
  .photo--nurses { left: 350px; top: 150px; width: 150px; height: 132px; background: linear-gradient(160deg, #f3f3f3, #a9c2da 50%, #2d5b9a); }
  .photo--team { left: 310px; top: 292px; width: 150px; height: 96px; background: linear-gradient(135deg, #eef0f1, #d8d2cc 55%, #b9c3cb); }
</style>
</head>
<body>
  <main class="spread">
    <section class="page page--left">
      <div class="section-tab">Contents</div>
      <h1 class="contents-title">Contents</h1>
      <ol class="toc toc--first">
        <li class="toc__item">
          <div class="toc__title"><span class="toc__num">7</span>Company profile</div>
          <p class="toc__text">Sed dapibus massa at elit ullamcorper tristique risus tincidunt.</p>
        </li>
        <li class="toc__item">
          <div class="toc__title"><span class="toc__num">9</span>Quality / Vision</div>
          <p class="toc__text">Sed dapibus massa at elit ullamcorper tristique risus tincidunt.</p>
        </li>
        <li class="toc__item">
          <div class="toc__title"><span class="toc__num">11</span>Continued education programs</div>
          <p class="toc__text">Sed dapibus massa at elit ullamcorper tristique risus tincidunt.</p>
        </li>
      </ol>
      <ol class="toc toc--second">
        <li class="toc__item">
          <div class="toc__title"><span class="toc__num">13</span>Main products</div>
          <p class="toc__text">Sed dapibus massa at elit ullamcorper tristique risus tincidunt.</p>
        </li>
        <li class="toc__item">
          <div class="toc__title"><span class="toc__num">15</span>Main partners</div>
          <p class="toc__text">Sed dapibus massa at elit ullamcorper tristique risus tincidunt.</p>
        </li>
        <li class="toc__item">
          <div class="toc__title"><span class="toc__num">17</span>Final stuff (creative final thoughts / considerations)</div>
          <p class="toc__text">Sed dapibus massa at elit ullamcorper tristique risus tincidunt.</p>
        </li>
      </ol>
      <div class="page-number">4</div>
    </section>

    <section class="page page--right">
      <div class="photo photo--doctor-notes" role="img" aria-label="Female doctor with stethoscope writing notes on a clipboard"><span class="photo__num">9</span></div>
      <div class="photo photo--dental" role="img" aria-label="Masked dentist examining a seated patient"><span class="photo__num">11</span></div>
      <div class="photo photo--patient-chat" role="img" aria-label="Nurse in teal scrubs talking with a patient"><span class="photo__num">7</span></div>
      <div class="photo photo--stethoscope" role="img" aria-label="Masked surgeon in green scrubs holding a stethoscope toward the camera"><span class="photo__num">15</span></div>
      <div class="section-tab">Contents</div>
      <div class="photo photo--nurses" role="img" aria-label="Two smiling nurses in blue uniforms pointing forward"><span class="photo__num">19</span></div>
      <div class="photo photo--team" role="img" aria-label="Smiling male doctor with colleagues in a bright clinic"><span class="photo__num">23</span></div>
      <div class="page-number">5</div>
    </section>
  </main>
</body>
</html>
```